Pacific Screen Trade Alliance is preparing a regular newsletter and needs a design

Our association is made up of media companies, TV stations and video on demand companies. As an association our role is to bring industry together to engage in government dialogues, fight video piracy and hold conferences and events. We are starting a regular newsletter to let our members know what activities we have been undertaking on their behalf and what upcoming activities there are. It will be a combination of text and pictures/ graphics. We have made a lot of changes to the association so we need a design which is professional looking, but also creative and future looking. It should also have a sense of entertainment given it is the video entertainment industry we represent. Attached is an example of a recent newsletter but would like to see something a little more dynamic and professional.

Target Market(s)

Executives in media companies

Font styles to use
Serif

Colors

Designer to choose colors to be used in the design.

Requirements
Must have
• A combination of text, photos and graphics in a modern, personable yet professional layout and design

```html
<!DOCTYPE html>
<html lang="en">
<head>
<meta charset="utf-8">
<title>Policy &amp; Piracy Newsletter – Spring 2019 Special Edition</title>
<link rel="stylesheet" href="https://fonts.googleapis.com/css2?family=Jost:wght@400;500;600&family=Oswald:wght@500;700&family=Anton&display=swap">
<style>
  :root{
    --brand-red:#e0232b;
    --brand-blue:#0d4f8b;
    --band-grey:#e7e7e9;
    --shadow-grey:#7a7c80;
    --ink:#1d1d1f;
    --paper:#ffffff;
    --backdrop:#e9e9ea;
    --photo-a:#2f5f8e;
    --photo-b:#8fa9c2;
  }
  *{margin:0;padding:0;box-sizing:border-box}
  html,body{width:1200px;height:1200px;overflow:hidden;background:var(--backdrop)}
  .newsletter{position:absolute;left:176px;top:0;width:848px;height:1200px;background:var(--paper);overflow:hidden;font-family:"Jost",sans-serif;color:var(--ink)}
  .shapes{position:absolute;inset:0}
  .masthead-name{position:absolute;left:48px;top:58px;font-family:"Jost",sans-serif;font-weight:600;font-size:24px;line-height:1.15;color:var(--brand-red);width:260px}
  .edition{position:absolute;left:88px;top:222px;color:#fff;font-size:14px;line-height:1.3;letter-spacing:.5px}
  .title-rule{position:absolute;left:140px;top:276px;width:360px;height:2px;background:#fff}
  .title-kicker{position:absolute;left:140px;top:292px;font-family:"Oswald",sans-serif;font-weight:700;font-size:30px;color:#fff;letter-spacing:1px}
  .title-main{position:absolute;left:140px;top:335px;font-family:"Oswald",sans-serif;font-weight:700;font-size:42px;color:#fff;letter-spacing:20px}
  .intro{position:absolute;left:480px;top:420px;width:335px;font-size:14.5px;line-height:1.45}
  .intro p+p{margin-top:14px}
  .issue-label{position:absolute;left:110px;top:530px;color:#fff;font-family:"Anton",sans-serif;line-height:.95}
  .issue-label .small{display:block;font-size:38px;letter-spacing:1px}
  .issue-label .big{display:block;font-size:92px;letter-spacing:1px}
  .briefs{position:absolute;left:30px;top:745px;width:790px;display:flex}
  .brief{flex:1;padding:0 16px;border-left:1.5px solid #555}
  .brief:first-child{border-left:none}
  .brief h3{font-family:"Oswald",sans-serif;font-weight:700;font-size:18px;margin-bottom:4px;letter-spacing:.3px}
  .brief p{font-size:13.5px;line-height:1.35}
  .credit{position:absolute;left:150px;top:930px;width:440px;border:1.5px solid var(--ink);padding:10px 14px;text-align:center;font-family:"Oswald",sans-serif;font-weight:500;font-size:14px;line-height:1.35}
  .partner{position:absolute;left:620px;top:925px;width:200px;display:flex;align-items:center;gap:10px;color:var(--brand-blue);font-weight:600;font-size:19px;line-height:1.1}
  .partner .dot{width:18px;height:18px;border-radius:50%;background:var(--brand-red);flex:none}
  .contact{position:absolute;display:flex;align-items:center;gap:10px;color:#fff;font-family:"Oswald",sans-serif;font-weight:500;font-size:16px}
  .contact svg{flex:none}
  .contact-web{left:500px;top:1128px}
  .contact-mail{left:500px;top:1072px}
  .contact-phone{left:40px;top:1146px;font-size:30px;letter-spacing:6px}
</style>
</head>
<body>
<main class="newsletter">
  <svg class="shapes" width="848" height="1200" viewBox="0 0 848 1200">
    <polygon class="title-band" points="0,180 620,180 560,420 0,420" fill="var(--brand-blue)"/>
    <polygon class="photo-accent" points="820,40 848,40 848,300 760,420 560,420 580,395 760,395 820,300" fill="#b9bcc2"/>
    <defs>
      <linearGradient id="photoTone" x1="0" y1="0" x2="1" y2="1">
        <stop offset="0" stop-color="var(--photo-b)"/>
        <stop offset="1" stop-color="var(--photo-a)"/>
      </linearGradient>
    </defs>
    <polygon class="feature-photo" role="img" aria-label="Photo of an investigator examining seized server racks and cabling marked with evidence tags" points="380,0 848,0 848,20 820,20 820,300 760,395 330,395 300,340" fill="url(#photoTone)"/>
    <polygon class="issue-shadow" points="160,455 420,455 500,585 420,715 160,715" fill="var(--shadow-grey)"/>
    <rect class="briefs-band" x="0" y="715" width="848" height="180" fill="var(--band-grey)"/>
    <polygon class="issue-hex" points="120,470 380,470 460,600 380,735 120,735 40,600" fill="var(--brand-red)"/>
    <polygon class="footer-blue" points="0,1100 848,1010 848,1200 0,1200" fill="var(--brand-blue)"/>
    <polygon class="footer-red" points="0,1120 390,1120 470,1200 0,1200" fill="var(--brand-red)"/>
  </svg>

  <div class="masthead-name">Pacific Screen Trade Alliance</div>

  <div class="edition">SPRING 2019<br>SPECIAL EDITION</div>
  <div class="title-rule"></div>
  <h1 class="title-kicker">POLICY &amp; PIRACY</h1>
  <div class="title-main">NEWSLETTER</div>

  <section class="intro">
    <p>The last few months have seen important antipiracy initiatives by several Asian governments. They are a clear indication that goverments are seriously grappling with the ISD/app piracy ecosystems. We've seen stepped-up enforcement, policy announcements, and legislative movement. (Now, if we could just get all of this in every country!)</p>
    <p>For everyone's convenience, we've brought together some short descriptions in this Special Edition of our Policy and Piracy Newsletter.</p>
  </section>

  <h2 class="issue-label"><span class="small">IN THIS</span><span class="big">ISSUE</span></h2>

  <section class="briefs">
    <article class="brief"><h3>SINGAPORE</h3><p>Ministry of Law announced a policy change banning the sale of ISDs and apps</p></article>
    <article class="brief"><h3>MALAYSIA</h3><p>Minister of Communications and Multimedia takes a strong stance against piracy</p></article>
    <article class="brief"><h3>PHILIPPINES</h3><p>New Online Infringement Act backed by Harbor Telecom and SRC</p></article>
    <article class="brief"><h3>THAILAND</h3><p>SCU conducted an intensive enforcement action against piracy syndicate</p></article>
  </section>

  <p class="credit">This Special Edition of the Policy and Piracy Newsletter was created in collaboration with the Screen Rights Coalition.</p>

  <div class="partner"><span class="dot"></span><span>Screen Rights Coalition</span></div>

  <div class="contact contact-mail">
    <svg width="30" height="20" viewBox="0 0 30 20"><rect x="1" y="1" width="28" height="18" fill="none" stroke="#fff" stroke-width="2"/><polyline points="1,1 15,11 29,1" fill="none" stroke="#fff" stroke-width="2"/></svg>
    <span>info@pacificscreen.org</span>
  </div>
  <div class="contact contact-web">
    <svg width="26" height="26" viewBox="0 0 26 26" fill="none" stroke="#fff" stroke-width="1.6"><circle cx="13" cy="13" r="11"/><ellipse cx="13" cy="13" rx="5" ry="11"/><line x1="2" y1="13" x2="24" y2="13"/><line x1="4" y1="7" x2="22" y2="7"/><line x1="4" y1="19" x2="22" y2="19"/></svg>
    <span>www.pacificscreen.org</span>
  </div>
  <div class="contact contact-phone">
    <svg width="30" height="30" viewBox="0 0 24 24"><path d="M6.6 10.8a15 15 0 0 0 6.6 6.6l2.2-2.2c.3-.3.7-.4 1-.2 1.1.4 2.3.6 3.6.6.6 0 1 .4 1 1V20c0 .6-.4 1-1 1A17 17 0 0 1 3 4c0-.6.4-1 1-1h3.5c.6 0 1 .4 1 1 0 1.3.2 2.5.6 3.6.1.3 0 .7-.2 1z" fill="#fff"/></svg>
    <span>6000 123 456</span>
  </div>
</main>
</body>
</html>
```